Up and coming Australian Systems Integrator needs a proposal template refresh

We need to update our proposal template and are looking for a fresh, modern, simple and elegant proposal template. We'd like to keep our existing logos if possible.
Quorvex is a privately owned company operating since 2006. Offices and technical staff located in Port Melbourne and Bendigo
Sustained, profitable growth year on year
Velmar strategic partner
Velmar Advanced Enterprise Network Architecture Specialisation
Velmar Advanced Security Architecture Specialisation
Velmar Advanced Collaboration Architecture Specialisation
Velmar Advanced Unified Computing Technology Specialisation
Velmar Advanced Data Centre Architecture Specialisation (in progress)
Velmar Gold Partner – Expect 2H2018
As well as being a Velmar partner we have a well established stable of other vendors such as Brandova, Teskaro, Haldenworth, ZEP, Mirvale Interactive, Dulm, TidePoint, KoMELDA Gate)
We are a top two provider of Velmar product/services in the Victorian healthcare sector.
Please feel free to use different colors and fonts as we feel the existing ones look dated.

```html
<!DOCTYPE html>
<html lang="en">
<head>
<meta charset="utf-8">
<title>Quorvex Proposal Template</title>
<link rel="stylesheet" href="https://fonts.googleapis.com/css2?family=Open+Sans:wght@400;600;700;800&family=Titillium+Web:wght@300;400;600&display=swap">
<style>
  :root {
    --stage: #b3b3b3;
    --paper: #ffffff;
    --brand-blue: #1f66a3;
    --brand-blue-deep: #1a5a91;
    --slate: #7f8a94;
    --band-grey: #9a9a9a;
    --ink: #222222;
    --muted: #6b6b6b;
    --warm-grey: #c9c1b1;
    --rule: #cfd8e2;
  }
  * { box-sizing: border-box; margin: 0; padding: 0; }
  html, body { width: 1152px; height: 1200px; overflow: hidden; }
  body {
    background: var(--stage);
    font-family: "Open Sans", Arial, sans-serif;
    color: var(--ink);
    position: relative;
  }
  .sheet-label {
    position: absolute;
    width: 355px;
    text-align: center;
    font-family: "Titillium Web", Arial, sans-serif;
    font-size: 24px;
    font-weight: 400;
    color: #111;
    letter-spacing: 0.5px;
  }
  .page {
    position: absolute;
    width: 355px;
    height: 500px;
    background: var(--paper);
    box-shadow: 0 10px 10px -6px rgba(0,0,0,0.35);
    overflow: hidden;
  }
  .page--cover { left: 162px; top: 70px; }
  .page--control { left: 626px; top: 70px; }
  .page--contents { left: 162px; top: 600px; }
  .page--company { left: 626px; top: 600px; }

  .bottom-band { position: absolute; left: 0; bottom: 0; width: 100%; height: 12px; }
  .bottom-band__blue { position: absolute; left: 0; top: 0; width: 237px; height: 12px; background: var(--brand-blue); }
  .bottom-band__grey { position: absolute; left: 242px; top: 0; right: 0; height: 12px; background: var(--slate); }

  /* cover */
  .cover-brand { position: absolute; top: 28px; left: 0; width: 100%; text-align: center; }
  .cover-brand__name {
    display: inline-flex; align-items: center; gap: 8px;
    font-family: "Titillium Web", Arial, sans-serif;
    font-weight: 600; font-size: 26px; color: var(--brand-blue); letter-spacing: 1px;
  }
  .cover-brand__square { width: 14px; height: 14px; background: var(--brand-blue); display: inline-block; }
  .cover-brand__tag { font-size: 5.5px; letter-spacing: 1.2px; color: var(--muted); margin-top: -2px; font-weight: 600; }
  .cover-photo {
    position: absolute; left: 0; top: 75px; width: 100%; height: 241px;
    background: linear-gradient(160deg, #d9d9d9 0%, #9c9c9c 35%, #5a5a5a 60%, #2c2c2c 100%);
  }
  .cover-title {
    position: absolute; left: 89px; top: 222px; width: 178px; height: 181px;
    background: rgba(31,102,163,0.93); color: #fff; text-align: center;
  }
  .cover-title__lead { margin-top: 42px; font-size: 23px; font-weight: 800; letter-spacing: 0.3px; line-height: 1; }
  .cover-title__sub { font-family: "Titillium Web", Arial, sans-serif; font-size: 15px; font-weight: 400; margin-top: 6px; }
  .cover-title__rule { width: 152px; height: 1px; background: rgba(255,255,255,0.45); margin: 7px auto 0; }
  .cover-title__doc { font-family: "Titillium Web", Arial, sans-serif; font-size: 24px; font-weight: 400; line-height: 1.05; margin-top: 10px; }
  .cover-title__doc span { display: block; }
  .cover-title__doc .accent { color: var(--warm-grey); }
  .cover-web { position: absolute; top: 464px; width: 100%; text-align: center; font-size: 10.5px; letter-spacing: 1.2px; color: #333; }

  /* inside header / footer */
  .top-band { position: absolute; left: 0; top: 0; width: 100%; height: 10px; background: var(--band-grey); }
  .top-band__blue { position: absolute; left: 24px; top: 10px; width: 300px; height: 7px; background: var(--brand-blue); }
  .confidential {
    position: absolute; top: 27px; left: 0; width: 100%; text-align: center;
    font-size: 7px; letter-spacing: 1px; color: #444;
  }
  .confidential span { display: inline-block; border-bottom: 1px solid #ddd; padding: 0 4px 3px; }
  .page-footer {
    position: absolute; left: 22px; right: 14px; top: 474px;
    display: flex; justify-content: space-between; align-items: center;
    font-size: 5.5px; font-weight: 700; color: #222;
  }
  .page-footer__brand { display: flex; align-items: center; gap: 3px; color: var(--brand-blue); font-family: "Titillium Web", Arial, sans-serif; font-size: 8px; font-weight: 600; }
  .page-footer__square { width: 5px; height: 5px; background: var(--brand-blue); }
  .page-footer__web { letter-spacing: 0.6px; }

  /* tables */
  .section-title {
    position: absolute; left: 0; width: 100%; text-align: center;
    font-size: 8px; color: var(--brand-blue); letter-spacing: 0.2px;
  }
  .grid-table {
    position: absolute; left: 66px; width: 223px;
    border-collapse: collapse; table-layout: fixed;
    border: 1px solid var(--brand-blue);
  }
  .grid-table th, .grid-table td {
    border-left: 1px solid var(--brand-blue); border-right: 1px solid var(--brand-blue);
    border-top: 1px solid var(--rule);
    font-size: 6.5px; font-weight: 600; color: #333;
  }
  .grid-table th { height: 24px; border-bottom: 1px solid var(--brand-blue); }
  .grid-table td { height: 22px; }

  /* contents */
  .toc-title { position: absolute; top: 78px; width: 100%; text-align: center; font-size: 8px; font-weight: 700; color: var(--brand-blue); }
  .toc-entry {
    position: absolute; left: 62px; width: 233px;
    display: flex; align-items: center; gap: 4px;
    font-size: 6.5px; color: var(--brand-blue);
  }
  .toc-entry__leader { flex: 1; border-bottom: 1px dashed var(--brand-blue); height: 0; margin: 0 4px; }

  /* company */
  .company-heading { position: absolute; top: 83px; left: 14px; display: flex; align-items: center; gap: 8px; font-size: 8px; font-weight: 700; color: var(--brand-blue); }
  .company-copy { position: absolute; top: 105px; left: 13px; right: 16px; font-size: 4.6px; line-height: 1.45; color: #555; }
  .company-copy p + p { margin-top: 6px; }
  .company-photo {
    position: absolute; left: 0; top: 180px; width: 100%; height: 257px;
    background: linear-gradient(180deg, #e9e2dc 0%, #cdbfae 40%, #7a6350 70%, #4a3a2e 100%);
  }
</style>
</head>
<body>

  <div class="sheet-label" style="left:162px; top:32px;">COVER</div>
  <div class="sheet-label" style="left:626px; top:32px;">INSIDE PAGE 1</div>
  <div class="sheet-label" style="left:162px; top:1117px;">INSIDE PAGE 2</div>
  <div class="sheet-label" style="left:626px; top:1117px;">INSIDE PAGE 3</div>

  <!-- Cover -->
  <section class="page page--cover">
    <div class="cover-brand">
      <div class="cover-brand__name"><span class="cover-brand__square"></span>QUORVEX</div>
      <div class="cover-brand__tag">NETWORK &amp; COMMUNICATIONS SOLUTIONS</div>
    </div>
    <div class="cover-photo" role="img" aria-label="Black and white photo of two business people shaking hands over a desk with a laptop and paperwork"></div>
    <div class="cover-title">
      <div class="cover-title__lead">AUSTRALIAN</div>
      <div class="cover-title__sub">SYSTEMS INTEGRATOR</div>
      <div class="cover-title__rule"></div>
      <div class="cover-title__doc"><span>PROPOSAL</span><span class="accent">TEMPLATE</span></div>
    </div>
    <div class="cover-web">www.quorvex.net.au</div>
    <div class="bottom-band"><div class="bottom-band__blue"></div><div class="bottom-band__grey"></div></div>
  </section>

  <!-- Inside page 1 -->
  <section class="page page--control">
    <div class="top-band"></div><div class="top-band__blue"></div>
    <div class="confidential"><span>COMMERCIAL-IN CONFIDENCE</span></div>

    <div class="section-title" style="top:48px;">DOCUMENT CONTROL</div>
    <table class="grid-table" style="top:63px;">
      <tr><th>Version&nbsp; Author</th><th>Description</th><th>Approval</th></tr>
      <tr><td></td><td></td><td></td></tr><tr><td></td><td></td><td></td></tr>
      <tr><td></td><td></td><td></td></tr><tr><td></td><td></td><td></td></tr>
    </table>

    <div class="section-title" style="top:186px;">DISTRIBUTION LIST</div>
    <table class="grid-table" style="top:201px;">
      <tr><th>Name</th><th>Company</th><th>Role</th></tr>
      <tr><td></td><td></td><td></td></tr><tr><td></td><td></td><td></td></tr>
      <tr><td></td><td></td><td></td></tr><tr><td></td><td></td><td></td></tr>
    </table>

    <div class="section-title" style="top:323px;">DEFINITIONS</div>
    <table class="grid-table" style="top:339px;">
      <tr><th>Term</th><th>Definition</th><th></th></tr>
      <tr><td></td><td></td><td></td></tr><tr><td></td><td></td><td></td></tr>
      <tr><td></td><td></td><td></td></tr><tr><td></td><td></td><td></td></tr>
    </table>

    <div class="page-footer">
      <span class="page-footer__brand"><span class="page-footer__square"></span>QUORVEX</span>
      <span>Network &amp; Communications Solutions</span>
      <span class="page-footer__web">www.quorvex.net.au</span>
    </div>
    <div class="bottom-band"><div class="bottom-band__blue"></div><div class="bottom-band__grey"></div></div>
  </section>

  <!-- Inside page 2 -->
  <section class="page page--contents">
    <div class="top-band"></div><div class="top-band__blue"></div>
    <div class="confidential"><span>COMMERCIAL-IN CONFIDENCE</span></div>
    <div class="toc-title">TABLE OF CONTENTS</div>
    <div class="toc-entry" style="top:104px;"><span>Heading 1</span><span class="toc-entry__leader"></span><span>3</span></div>
    <div class="toc-entry" style="top:136px;"><span>Heading 2</span><span class="toc-entry__leader"></span><span>3</span></div>
    <div class="toc-entry" style="top:176px;"><span>Heading 3</span><span class="toc-entry__leader"></span><span>3</span></div>
    <div class="page-footer">
      <span class="page-footer__brand"><span class="page-footer__square"></span>QUORVEX</span>
      <span>Network &amp; Communications Solutions</span>
      <span class="page-footer__web">www.quorvex.net.au</span>
    </div>
    <div class="bottom-band"><div class="bottom-band__blue"></div><div class="bottom-band__grey"></div></div>
  </section>

  <!-- Inside page 3 -->
  <section class="page page--company">
    <div class="top-band"></div><div class="top-band__blue"></div>
    <div class="confidential"><span>COMMERCIAL-IN CONFIDENCE</span></div>
    <div class="company-heading">
      <svg width="16" height="11" viewBox="0 0 16 11" aria-hidden="true">
        <rect x="0.5" y="3" width="5" height="7.5" fill="none" stroke="#8a8a8a"/>
        <rect x="5.5" y="0.5" width="6" height="10" fill="none" stroke="#8a8a8a"/>
        <rect x="11.5" y="4" width="4" height="6.5" fill="none" stroke="#8a8a8a"/>
      </svg>
      OUR COMPANY
    </div>
    <div class="company-copy">
      <p>We service a wide range of customers from SMB through to Enterprise, and have developed a strong reputation for delivering high quality, world-class solutions for our client base. Quorvex operate across multiple industry sectors including Health &amp; Aged Care, Government, Utility, Finance, Agriculture, Education and Manufacturing.</p>
      <p>Our point of difference comes from our client interaction, collaborative nature, and flexible approach to service delivery, resulting in greater value and satisfaction for our clients. We collaborate closely with our clients to understand their business requirements and organisational challenges, using our experience and expertise to map solutions to organisational needs to provide tailored, functional options to our clients.</p>
    </div>
    <div class="company-photo" role="img" aria-label="Photo of an empty boardroom with a long table, leather chairs and floor-to-ceiling windows"></div>
    <div class="page-footer">
      <span class="page-footer__brand"><span class="page-footer__square"></span>QUORVEX</span>
      <span>Network &amp; Communications Solutions</span>
      <span class="page-footer__web">www.quorvex.net.au</span>
    </div>
    <div class="bottom-band"><div class="bottom-band__blue"></div><div class="bottom-band__grey"></div></div>
  </section>

</body>
</html>
```